Business cards — need something that creates “wow” factor

Need a sleek and clean looking business card. Something that is clear and consise. These business cards are for my painting business and hundreds will be placed in the Dallas area between all Halverd Pemberton paint stored. These card really need to stick out! Open to any and all ideas...

Target Market(s)

Residential clientele

Industry/Entity Type

Painting

Contact Information for Business Card

Dorian Vakelby
Owner

382.516.2074

Web: Mesahuepainting.example (still under construction)
Mesahuepainting@mailbox.example

Font styles to use
Sans Serif

Colors

Designer to choose colors to be used in the design.

Requirements
Must have
• My name, number, website, email, Socialpage
• and “100% customer satisfaction guaranteed”
• Socialpage.example/Mesahuepainting/
Nice to have
• Listed services
• Interior/exterior painting
• Drywall repair/texture
• Fence staining/refinishing
• Concrete staining
• Epoxy flooring
• Pressure washing

```html
<!DOCTYPE html>
<html lang="en">
<head>
<meta charset="utf-8">
<title>Mesa Hue Painting — Business Card</title>
<link href="https://fonts.googleapis.com/css2?family=Montserrat:wght@300;400;500;600&display=swap" rel="stylesheet">
<style>
  :root {
    --page: #e9e9e9;
    --card: #f4f4f4;
    --card-edge: #8a8a8a;
    --ink: #2b2b2b;
    --muted: #9a9a9a;
    --teal: #17a589;
    --rule: #3a3a3a;
    --ghost: #e7e7e7;
  }
  * { box-sizing: border-box; margin: 0; padding: 0; }
  html, body { width: 1200px; height: 1200px; overflow: hidden; }
  body {
    background: var(--page);
    font-family: "Montserrat", sans-serif;
    color: var(--ink);
    position: relative;
  }
  .card {
    position: absolute;
    top: 432px;
    width: 560px;
    height: 336px;
    background: var(--card);
    border: 1.5px solid var(--card-edge);
    overflow: hidden;
  }
  .card--front { left: 30px; }
  .card--back { left: 610px; }

  .paint-trail { position: absolute; }
  .paint-trail--top { left: 258px; top: 18px; width: 286px; height: 82px; }
  .paint-trail--bottom { left: 20px; top: 234px; width: 292px; height: 86px; }

  .brand {
    position: absolute;
    left: 0; right: 0;
    top: 128px;
    text-align: center;
  }
  .brand__name {
    font-size: 50px;
    font-weight: 400;
    letter-spacing: 3px;
    line-height: 1;
  }
  .brand__tagline {
    margin-top: 10px;
    font-size: 9px;
    font-weight: 300;
    color: var(--muted);
  }
  .front__url {
    position: absolute;
    right: 36px;
    bottom: 36px;
    font-size: 12px;
    font-weight: 500;
  }

  .back__ghost {
    position: absolute;
    left: 22px;
    bottom: -12px;
    font-size: 60px;
    font-weight: 600;
    letter-spacing: 2px;
    line-height: 1;
    color: var(--ghost);
    white-space: nowrap;
  }
  .identity {
    position: absolute;
    left: 96px;
    top: 100px;
    width: 196px;
  }
  .identity__brand {
    font-size: 26px;
    font-weight: 400;
    letter-spacing: 1.5px;
    line-height: 1;
  }
  .identity__name {
    margin-top: 14px;
    font-size: 16px;
    font-weight: 500;
    color: var(--teal);
  }
  .identity__role {
    font-size: 12px;
    font-weight: 500;
  }
  .identity__guarantee {
    margin-top: 12px;
    font-size: 9px;
    font-weight: 500;
    color: var(--teal);
    line-height: 1.3;
  }
  .contact-group {
    position: absolute;
    left: 302px;
    border-left: 1.5px solid var(--rule);
    padding-left: 15px;
    font-size: 11.5px;
    font-weight: 500;
    line-height: 1.5;
  }
  .contact-group--phone { top: 46px; height: 30px; }
  .contact-group--web { top: 96px; }
  .contact-group--services { top: 166px; line-height: 1.32; }
  .contact-group__icons { display: flex; gap: 4px; align-items: center; height: 14px; }
  .contact-group__value { margin-top: 2px; }
  .services__heading { font-weight: 500; }
  .services { list-style: none; }
</style>
</head>
<body>

<section class="card card--front" aria-label="Card front">
  <svg class="paint-trail paint-trail--top" viewBox="0 0 286 82" role="img" aria-label="Trail of overlapping colourful paint hexagons">
    <defs>
      <linearGradient id="trailTop" x1="0" x2="1" y1="0" y2="0">
        <stop offset="0" stop-color="#e6499a" stop-opacity="0.5"/>
        <stop offset="0.25" stop-color="#4cc3c9" stop-opacity="0.8"/>
        <stop offset="0.45" stop-color="#9ccc3c"/>
        <stop offset="0.6" stop-color="#f5d327"/>
        <stop offset="0.75" stop-color="#f0504a"/>
        <stop offset="0.88" stop-color="#e6499a"/>
        <stop offset="1" stop-color="#5b3a9e"/>
      </linearGradient>
    </defs>
    <path d="M0 40 Q60 22 140 28 L200 20 L286 4 L286 80 L240 80 L200 62 L140 50 Q60 46 0 44 Z" fill="url(#trailTop)"/>
  </svg>

  <svg class="paint-trail paint-trail--bottom" viewBox="0 0 292 86" role="img" aria-label="Trail of overlapping colourful paint hexagons">
    <defs>
      <linearGradient id="trailBottom" x1="0" x2="1" y1="0" y2="0">
        <stop offset="0" stop-color="#5b3a9e"/>
        <stop offset="0.15" stop-color="#e6499a"/>
        <stop offset="0.3" stop-color="#f0504a"/>
        <stop offset="0.45" stop-color="#f5d327"/>
        <stop offset="0.6" stop-color="#9ccc3c"/>
        <stop offset="0.72" stop-color="#4cc3c9"/>
        <stop offset="0.85" stop-color="#8a63b8" stop-opacity="0.8"/>
        <stop offset="1" stop-color="#e6499a" stop-opacity="0.6"/>
      </linearGradient>
    </defs>
    <path d="M0 8 L40 4 L100 20 L180 14 Q240 26 292 36 L292 42 Q240 44 180 48 L120 60 L60 70 L30 86 L0 86 Z" fill="url(#trailBottom)"/>
  </svg>

  <div class="brand">
    <div class="brand__name">MESA HUE</div>
    <div class="brand__tagline">Commercial | Residential | Interior | Exterior</div>
  </div>

  <div class="front__url">www.Mesahuepainting.example</div>
</section>

<section class="card card--back" aria-label="Card back">
  <div class="back__ghost" aria-hidden="true">MESA HUE</div>

  <div class="identity">
    <div class="identity__brand">MESA HUE</div>
    <div class="identity__name">Dorian Vakelby</div>
    <div class="identity__role">Owner</div>
    <div class="identity__guarantee">100% customer satisfaction guaranteed</div>
  </div>

  <div class="contact-group contact-group--phone">
    <div class="contact-group__icons">
      <svg width="10" height="10" viewBox="0 0 24 24" aria-label="Phone"><path fill="#2b2b2b" d="M6.6 10.8a15.1 15.1 0 006.6 6.6l2.2-2.2c.3-.3.7-.4 1-.2 1.1.4 2.3.6 3.6.6.6 0 1 .4 1 1V20c0 .6-.4 1-1 1A17 17 0 013 4c0-.6.4-1 1-1h3.5c.6 0 1 .4 1 1 0 1.3.2 2.5.6 3.6.1.3 0 .7-.2 1z"/></svg>
    </div>
    <div class="contact-group__value">382.516.2074</div>
  </div>

  <div class="contact-group contact-group--web">
    <div class="contact-group__icons">
      <svg width="13" height="10" viewBox="0 0 26 20" aria-label="Email"><rect x="1" y="1" width="24" height="18" fill="#17a589"/><path d="M1 1 L13 11 L25 1" stroke="#f4f4f4" stroke-width="2" fill="none"/></svg>
      <svg width="10" height="10" viewBox="0 0 10 10" aria-label="Social page"><rect width="10" height="10" fill="#2f4f9a"/></svg>
    </div>
    <div class="contact-group__value">Mesahuepainting@mailbox.example<br>Socialpage.example/Mesahuepainting/</div>
  </div>

  <div class="contact-group contact-group--services">
    <div class="services__heading">Listed services</div>
    <ul class="services">
      <li>- Interior/exterior painting</li>
      <li>- Drywall repair/texture</li>
      <li>- Fence staining/refinishing</li>
      <li>- Concrete staining</li>
      <li>- Epoxy flooring</li>
      <li>- Pressure washing</li>
    </ul>
  </div>
</section>

</body>
</html>
```